Redesign one screen in a mobile app

I have an app called Toasts and Tallies (available on iOS and Android). This app allows wedding guests to bet on things that happen during a wedding they are attending (think: will the groom cry when the bride walks down the aisle...). The event is set up by someone called the "event leader", typically this is the bride or the groom.

Once event details, bets, and $ values of the bets are entered, the event leader publishes the event and gets to the event detail homescreen, where they can manage their event. The three main things they can do are:

1.) Share the event with other guests to join in the betting.
2.) Edit the event -- add, change, or delete bets.
3.) Add a co-organizer. If you are the bride or the groom, you want someone else managing the event on your wedding day.

I'd like to redesign this page, make it simpler, and *focus attention on sharing the event.* The biggest goal of this page is getting event leaders to share the event. We want them to invite as many wedding guests as possible.

To that end, I would like to also introducing "sharing tiers" to entice more sharing and I'd like this to be something event leaders can easily see once they hit the event homescreen. Tiers are as follows:
Share with 1 guest, unlock co-organizer feature.
Share with 5 guests, unlock physical placard with custom QR code.
Share with 10 guests, we split our proceeds with the bride and groom.
Share with 20 guests, you are entered into $250 monthly raffle.

Some additional requests:
+ Please do not use current fonts. We want new fonts that are cleaner.
+ Share options should stay the same (copy, share, QR code)
+ Need to keep "help" question mark on page as well.
+ Maintain colors generally. Red button color must be kept as is because it's used throughout app. Slight variations to other colors OK.
+ Navigation at bottom must remain.
+ Feel free to add moving elements as well, like gifs.
+ Final design delivered in Figma.
Updates

Submissions need to be app designs. Not webpages.

The current actions shown on the page need to remain - share event, edit event, add a Co-Organizer. But the goal of the design is to make the page simpler, not more complicated.

Sharing tiers can be a separate screen, linked from the event home screen. This information does not need to live on the same page!

Target Market(s)

25-40 year olds

Industry/Entity Type

Mobile Apps - Betting

Font styles to use
Sans Serif
Other font styles liked:
• I like poppins, but open to other options.

Requirements
Must have
• Fun design that focuses on sharing an event. Design delievered in Figma.

```html
<!DOCTYPE html>
<html lang="en">
<head>
<meta charset="utf-8">
<title>Toasts and Tallies – Event Home</title>
<link href="https://fonts.googleapis.com/css2?family=Nunito+Sans:wght@400;600;700&display=swap" rel="stylesheet">
<style>
  :root{
    --bg:#dcd8c8;
    --screen:#f3f4f8;
    --card:#f8f8fb;
    --chip:#eeeff4;
    --ink:#2b2d33;
    --muted:#55575e;
    --line:#d9dae0;
    --red:#e0604f;
    --red-light:#e6817a;
    --white:#ffffff;
  }
  *{box-sizing:border-box;margin:0;padding:0}
  html,body{width:1200px;height:1200px;overflow:hidden;background:var(--bg);
    font-family:"Nunito Sans",Arial,sans-serif;color:var(--ink)}
  .stage{position:relative;width:1200px;height:1200px}
  .screen{position:absolute;top:261px;width:528px;height:1150px;background:var(--screen);
    border-radius:60px;overflow:hidden;transform:scale(.621);transform-origin:0 0;
    box-shadow:0 20px 40px rgba(60,50,30,.18)}
  .screen--details{left:175px}
  .screen--sharing{left:692px}
  .abs{position:absolute}
  .status-time{left:40px;top:24px;font-size:18px;color:var(--muted)}
  .status-icons{right:36px;top:28px}
  .round-btn{width:64px;height:64px;border-radius:50%;background:var(--white);display:flex;align-items:center;justify-content:center;top:73px}
  .round-btn--back{left:28px}
  .round-btn--help{left:438px}
  .card{left:27px;width:475px;background:var(--card);border-radius:24px}
  .card-title{font-size:21px;font-weight:600;color:var(--ink)}
  .count-chip{height:36px;border-radius:18px;background:var(--chip);display:flex;align-items:center;gap:8px;padding:0 18px;font-size:19px}
  .photo{left:25px;top:80px;width:425px;height:143px;border-radius:12px;
    background:linear-gradient(180deg,#c8b9a0 0%,#efe6dc 45%,#e9e0d6 70%,#8a7058 100%)}
  .event-name{left:50px;top:240px;font-size:26px;font-weight:400}
  .meta{left:50px;display:flex;align-items:center;gap:14px;font-size:21px}
  .divider{height:2px;background:var(--line)}
  .btn-primary{height:46px;border-radius:14px;background:linear-gradient(90deg,var(--red-light),var(--red));
    color:var(--white);display:flex;align-items:center;justify-content:center;gap:10px;font-size:16px}
  .tier-icon,.tier-guests,.tier-perk{height:49px;border-radius:12px;background:var(--chip);display:flex;align-items:center;justify-content:center}
  .tier-icon{width:50px}
  .tier-guests{width:100px;font-size:15px;font-weight:700}
  .tier-perk{width:225px;font-size:12.5px;text-align:center}
  .tier-perk--small{font-size:10px}
  .share-btn{width:134px;height:60px;border-radius:14px;background:var(--red);color:var(--white);
    display:flex;align-items:center;justify-content:center;gap:10px;font-size:16px}
  .organizer{left:27px;top:69px;width:424px;height:92px;border-radius:46px;background:var(--chip)}
  .avatar{left:28px;top:16px;width:60px;height:60px;border-radius:50%;background:var(--white);display:flex;align-items:center;justify-content:center}
  .organizer-name{left:124px;top:33px;font-size:19px}
  .bottom-nav{left:0;top:1030px;width:528px;height:120px;background:var(--white);border-radius:30px 30px 0 0}
  .nav-home{left:79px;top:28px;width:70px;height:70px;border-radius:50%;background:var(--red);display:flex;align-items:center;justify-content:center}
  .nav-item{top:46px}
</style>
</head>
<body>
<div class="stage">

  <!-- Event details screen -->
  <section class="screen screen--details">
    <div class="abs status-time">9:30</div>
    <svg class="abs status-icons" width="58" height="20" viewBox="0 0 58 20"><path d="M0 6 Q10 -2 20 6 L10 18Z" fill="#ddd"/><path d="M24 18 L38 4 V18Z" fill="#333"/><rect x="46" y="2" width="9" height="16" rx="2" fill="#333"/></svg>
    <div class="abs round-btn round-btn--back"><svg width="28" height="20" viewBox="0 0 28 20"><path d="M26 10H3M11 2 3 10l8 8" fill="none" stroke="#333" stroke-width="2.4" stroke-linecap="round" stroke-linejoin="round"/></svg></div>
    <div class="abs round-btn round-btn--help"><svg width="40" height="40" viewBox="0 0 40 40"><circle cx="20" cy="20" r="17" fill="none" stroke="#333" stroke-width="2.6"/><path d="M15 15a5 5 0 1 1 7 4.6c-1.4.7-2 1.6-2 3.2v1" fill="none" stroke="#333" stroke-width="2.6" stroke-linecap="round"/><circle cx="20" cy="29" r="1.8" fill="#333"/></svg></div>

    <div class="abs card" style="top:160px;height:540px">
      <div class="abs card-title" style="left:25px;top:28px">Event Details</div>
      <div class="abs count-chip" style="right:25px;top:24px"><svg width="26" height="24" viewBox="0 0 26 24"><g fill="none" stroke="#333" stroke-width="2" stroke-linejoin="round"><rect x="3" y="5" width="12" height="17" rx="1.5" transform="rotate(-12 9 13)"/><path d="M13 3l9 2-3 17-7-1.5"/></g></svg>8</div>
      <div class="abs photo" role="img" aria-label="Photo of the wedding reception hall with round tables and chairs"></div>
      <div class="abs event-name">Nora &amp; Eli’s Wedding</div>
      <svg class="abs" style="left:390px;top:240px" width="34" height="32" viewBox="0 0 24 23"><path d="M12 1l3.2 6.6 7.3 1-5.3 5.1 1.3 7.3L12 17.6 5.5 21l1.3-7.3L1.5 8.6l7.3-1z" fill="var(--red)"/></svg>
      <div class="abs meta" style="top:290px"><svg width="26" height="28" viewBox="0 0 26 28"><path d="M13 26s-9-8-9-14a9 9 0 0 1 18 0c0 6-9 14-9 14z" fill="none" stroke="#333" stroke-width="2.2"/><circle cx="13" cy="12" r="3.5" fill="none" stroke="#333" stroke-width="2.2"/></svg>Missouri</div>
      <div class="abs meta" style="top:333px"><svg width="26" height="28" viewBox="0 0 26 28"><rect x="2" y="5" width="22" height="21" rx="2.5" fill="none" stroke="#333" stroke-width="2.2"/><path d="M2 11h22M8 2v6M18 2v6M11 18h4v4" fill="none" stroke="#333" stroke-width="2.2"/></svg>February 08, 2024</div>
      <div class="abs meta" style="top:375px"><svg width="26" height="28" viewBox="0 0 26 28"><circle cx="13" cy="14" r="11" fill="none" stroke="#333" stroke-width="2.2"/><path d="M13 8v6l4 3" fill="none" stroke="#333" stroke-width="2.2" stroke-linecap="round"/></svg>05:00 PM - 8:00 PM</div>
      <div class="abs divider" style="left:25px;top:437px;width:420px"></div>
      <div class="abs btn-primary" style="left:25px;top:465px;width:425px"><svg width="22" height="22" viewBox="0 0 22 22"><path d="M14 3l5 5L8 19H3v-5z" fill="none" stroke="#fff" stroke-width="1.8" stroke-linejoin="round"/></svg>Edit Your Event</div>
    </div>

    <div class="abs card" style="top:727px;height:400px">
      <div class="abs card-title" style="left:27px;top:27px">Sharing Tiers</div>
      <div class="abs count-chip" style="right:25px;top:21px"><svg width="26" height="22" viewBox="0 0 26 22"><path d="M15 2l9 8-9 8v-5C8 13 4 15 2 20c0-8 5-13 13-13z" fill="none" stroke="#333" stroke-width="2" stroke-linejoin="round"/></svg>12</div>
      <div class="abs" style="left:25px;top:78px;display:grid;grid-template-columns:50px 100px 225px;column-gap:25px;row-gap:15px">
        <div class="tier-icon"><svg width="28" height="27" viewBox="0 0 24 23"><path d="M12 1.5l3.1 6.4 7 1-5.1 5 1.2 7L12 17.6l-6.2 3.3 1.2-7-5.1-5 7-1z" fill="none" stroke="var(--red)" stroke-width="1.8" stroke-linejoin="round"/></svg></div>
        <div class="tier-guests">1 Guest</div><div class="tier-perk">unlock co-organizer feature</div>
        <div class="tier-icon"><svg width="28" height="27" viewBox="0 0 24 23"><path d="M12 1.5l3.1 6.4 7 1-5.1 5 1.2 7L12 17.6l-6.2 3.3 1.2-7-5.1-5 7-1z" fill="none" stroke="var(--red)" stroke-width="1.8" stroke-linejoin="round"/><path d="M12 1.5v16.1l-6.2 3.3 1.2-7-5.1-5 7-1z" fill="var(--red)"/></svg></div>
        <div class="tier-guests">5 Guests</div><div class="tier-perk">Placard with custom QR code</div>
        <div class="tier-icon"><svg width="28" height="27" viewBox="0 0 24 23"><path d="M12 1.5l3.1 6.4 7 1-5.1 5 1.2 7L12 17.6l-6.2 3.3 1.2-7-5.1-5 7-1z" fill="var(--red)"/></svg></div>
        <div class="tier-guests">10 Guests</div><div class="tier-perk tier-perk--small">Split proceeds with the bride and groom</div>
        <div class="tier-icon"><svg width="30" height="28" viewBox="0 0 30 28"><g fill="var(--red)"><path d="M15 1l2.2 4.4 4.8.7-3.5 3.4.8 4.8L15 12l-4.3 2.3.8-4.8L8 6.1l4.8-.7z"/><path d="M8 13l2.2 4.4 4.8.7-3.5 3.4.8 4.8L8 24l-4.3 2.3.8-4.8L1 18.1l4.8-.7z"/><path d="M22 13l2.2 4.4 4.8.7-3.5 3.4.8 4.8L22 24l-4.3 2.3.8-4.8L15 18.1l4.8-.7z"/></g></svg></div>
        <div class="tier-guests">20 Guests</div><div class="tier-perk">Entered into $250 monthly raffle</div>
      </div>
    </div>

    <nav class="abs bottom-nav">
      <div class="abs nav-home"><svg width="32" height="30" viewBox="0 0 32 30"><path d="M4 14L16 4l12 10v13H4z" fill="none" stroke="#fff" stroke-width="2.4" stroke-linejoin="round"/><path d="M13 27v-7h6v7" fill="none" stroke="#fff" stroke-width="2.4"/></svg></div>
      <svg class="abs nav-item" style="left:249px" width="34" height="32" viewBox="0 0 26 24"><g fill="none" stroke="#333" stroke-width="1.8" stroke-linejoin="round"><rect x="3" y="5" width="12" height="17" rx="1.5" transform="rotate(-12 9 13)"/><path d="M13 3l9 2-3 17-7-1.5"/></g></svg>
      <svg class="abs nav-item" style="left:396px" width="36" height="32" viewBox="0 0 36 32"><path d="M2 30h32M3 30V16h9v14M12 30V4h11v26M23 30V13h10v17" fill="none" stroke="#333" stroke-width="2" stroke-linejoin="round"/></svg>
    </nav>
  </section>

  <!-- Sharing screen -->
  <section class="screen screen--sharing">
    <div class="abs card" style="top:155px;height:130px;border-radius:0 0 24px 24px">
      <div class="abs divider" style="left:25px;top:26px;width:420px"></div>
      <div class="abs btn-primary" style="left:25px;top:53px;width:425px"><svg width="22" height="22" viewBox="0 0 22 22"><path d="M14 3l5 5L8 19H3v-5z" fill="none" stroke="#fff" stroke-width="1.8" stroke-linejoin="round"/></svg>Edit Your Event</div>
    </div>
    <div class="abs status-time">9:30</div>
    <svg class="abs status-icons" width="58" height="20" viewBox="0 0 58 20"><path d="M0 6 Q10 -2 20 6 L10 18Z" fill="#ddd"/><path d="M24 18 L38 4 V18Z" fill="#333"/><rect x="46" y="2" width="9" height="16" rx="2" fill="#333"/></svg>
    <div class="abs round-btn round-btn--back"><svg width="28" height="20" viewBox="0 0 28 20"><path d="M26 10H3M11 2 3 10l8 8" fill="none" stroke="#333" stroke-width="2.4" stroke-linecap="round" stroke-linejoin="round"/></svg></div>
    <div class="abs round-btn round-btn--help"><svg width="40" height="40" viewBox="0 0 40 40"><circle cx="20" cy="20" r="17" fill="none" stroke="#333" stroke-width="2.6"/><path d="M15 15a5 5 0 1 1 7 4.6c-1.4.7-2 1.6-2 3.2v1" fill="none" stroke="#333" stroke-width="2.6" stroke-linecap="round"/><circle cx="20" cy="29" r="1.8" fill="#333"/></svg></div>

    <div class="abs card" style="top:310px;height:478px">
      <div class="abs card-title" style="left:29px;top:26px">Sharing Tiers</div>
      <div class="abs count-chip" style="right:25px;top:20px"><svg width="26" height="22" viewBox="0 0 26 22"><path d="M15 2l9 8-9 8v-5C8 13 4 15 2 20c0-8 5-13 13-13z" fill="none" stroke="#333" stroke-width="2" stroke-linejoin="round"/></svg>12</div>
      <div class="abs" style="left:25px;top:78px;display:grid;grid-template-columns:50px 100px 225px;column-gap:25px;row-gap:15px">
        <div class="tier-icon"><svg width="28" height="27" viewBox="0 0 24 23"><path d="M12 1.5l3.1 6.4 7 1-5.1 5 1.2 7L12 17.6l-6.2 3.3 1.2-7-5.1-5 7-1z" fill="none" stroke="var(--red)" stroke-width="1.8" stroke-linejoin="round"/></svg></div>
        <div class="tier-guests">1 Guest</div><div class="tier-perk">unlock co-organizer feature</div>
        <div class="tier-icon"><svg width="28" height="27" viewBox="0 0 24 23"><path d="M12 1.5l3.1 6.4 7 1-5.1 5 1.2 7L12 17.6l-6.2 3.3 1.2-7-5.1-5 7-1z" fill="none" stroke="var(--red)" stroke-width="1.8" stroke-linejoin="round"/><path d="M12 1.5v16.1l-6.2 3.3 1.2-7-5.1-5 7-1z" fill="var(--red)"/></svg></div>
        <div class="tier-guests">5 Guests</div><div class="tier-perk">Placard with custom QR code</div>
        <div class="tier-icon"><svg width="28" height="27" viewBox="0 0 24 23"><path d="M12 1.5l3.1 6.4 7 1-5.1 5 1.2 7L12 17.6l-6.2 3.3 1.2-7-5.1-5 7-1z" fill="var(--red)"/></svg></div>
        <div class="tier-guests">10 Guests</div><div class="tier-perk tier-perk--small">Split proceeds with the bride and groom</div>
        <div class="tier-icon"><svg width="30" height="28" viewBox="0 0 30 28"><g fill="var(--red)"><path d="M15 1l2.2 4.4 4.8.7-3.5 3.4.8 4.8L15 12l-4.3 2.3.8-4.8L8 6.1l4.8-.7z"/><path d="M8 13l2.2 4.4 4.8.7-3.5 3.4.8 4.8L8 24l-4.3 2.3.8-4.8L1 18.1l4.8-.7z"/><path d="M22 13l2.2 4.4 4.8.7-3.5 3.4.8 4.8L22 24l-4.3 2.3.8-4.8L15 18.1l4.8-.7z"/></g></svg></div>
        <div class="tier-guests">20 Guests</div><div class="tier-perk">Entered into $250 monthly raffle</div>
      </div>
      <div class="abs divider" style="left:28px;top:351px;width:420px"></div>
      <div class="abs" style="left:25px;top:380px;display:flex;gap:11px">
        <div class="share-btn"><svg width="24" height="24" viewBox="0 0 24 24"><g fill="none" stroke="#fff" stroke-width="1.8" stroke-linecap="round"><path d="M10 14a5 5 0 0 0 7 0l3.5-3.5a5 5 0 0 0-7-7L12 5"/><path d="M14 10a5 5 0 0 0-7 0l-3.5 3.5a5 5 0 0 0 7 7L12 19"/></g></svg>Copy</div>
        <div class="share-btn"><svg width="24" height="26" viewBox="0 0 24 26"><g fill="none" stroke="#fff" stroke-width="1.8"><circle cx="19" cy="4" r="3"/><circle cx="5" cy="13" r="3"/><circle cx="19" cy="22" r="3"/><path d="M8 11.5l8-6M8 14.5l8 6"/></g></svg>Share</div>
        <div class="share-btn"><svg width="24" height="24" viewBox="0 0 24 24"><g fill="none" stroke="#fff" stroke-width="1.8"><rect x="2" y="2" width="8" height="8" rx="1"/><rect x="14" y="2" width="8" height="8" rx="1"/><rect x="2" y="14" width="8" height="8" rx="1"/><path d="M14 14h3v3h-3zM20 14v3M14 20h3M20 20v2h2"/></g></svg>QR Code</div>
      </div>
    </div>

    <div class="abs card" style="top:815px;height:190px">
      <div class="abs card-title" style="left:25px;top:23px">Event Organizers</div>
      <svg class="abs" style="left:426px;top:20px" width="28" height="28" viewBox="0 0 28 28"><circle cx="14" cy="14" r="12" fill="none" stroke="#222" stroke-width="2"/><path d="M14 8v12M8 14h12" stroke="#222" stroke-width="2" stroke-linecap="round"/></svg>
      <div class="abs organizer">
        <div class="abs avatar"><svg width="48" height="48" viewBox="0 0 48 48"><circle cx="24" cy="24" r="21" fill="none" stroke="#2b2d33" stroke-width="4"/><circle cx="24" cy="19" r="7" fill="#2b2d33"/><path d="M11 38c3-7 8-9 13-9s10 2 13 9" fill="#2b2d33"/></svg></div>
        <div class="abs organizer-name">Owen Marsh</div>
        <svg class="abs" style="left:376px;top:36px" width="28" height="20" viewBox="0 0 28 20"><path d="M2 4l6 6 6-8 6 8 6-6-2 14H4z" fill="var(--red)"/></svg>
      </div>
    </div>

    <nav class="abs bottom-nav">
      <div class="abs nav-home"><svg width="32" height="30" viewBox="0 0 32 30"><path d="M4 14L16 4l12 10v13H4z" fill="none" stroke="#fff" stroke-width="2.4" stroke-linejoin="round"/><path d="M13 27v-7h6v7" fill="none" stroke="#fff" stroke-width="2.4"/></svg></div>
      <svg class="abs nav-item" style="left:249px" width="34" height="32" viewBox="0 0 26 24"><g fill="none" stroke="#333" stroke-width="1.8" stroke-linejoin="round"><rect x="3" y="5" width="12" height="17" rx="1.5" transform="rotate(-12 9 13)"/><path d="M13 3l9 2-3 17-7-1.5"/></g></svg>
      <svg class="abs nav-item" style="left:396px" width="36" height="32" viewBox="0 0 36 32"><path d="M2 30h32M3 30V16h9v14M12 30V4h11v26M23 30V13h10v17" fill="none" stroke="#333" stroke-width="2" stroke-linejoin="round"/></svg>
    </nav>
  </section>

</div>
</body>
</html>
```